Client questionnaire

KR Allied Group (www.krallied.com.au) needs a document designed to bring out as a questionnaire to speak with potential clients. Sales staff and planners will use this in introductions to ask basic questions but to also scribble notes and draw pictures on top of the graph.
I've attached two files which are the content that we wish to include.
1. Financial life cycle: this has two pages. Please design it so that the financial snap shot is on a different page than the lifecycle and graph. I will leave it to the designer to decide whether landscape or portrait is best - please ensure though that they are both landscape or both portrait on this document as they will be printed back to back on the same sheet.
2. Goals diagram - please theme this in the same way as the above document.
3. I've attached the logo to be used too - filename: KRAlliedgroup.eps

Industry/Entity Type

Group

```html
<!DOCTYPE html>
<html lang="en">
<head>
<meta charset="utf-8">
<title>KR Allied Group – Client Questionnaire</title>
<link rel="stylesheet" href="https://fonts.googleapis.com/css2?family=Montserrat:wght@300;400&display=swap">
<style>
  :root {
    --ink: #4a4a4c;
    --band: #4b4b4d;
    --grey: #9b9b9d;
    --grey-light: #a3a3a5;
    --paper: #ffffff;
    --frame: #5a5a5c;
  }
  * { box-sizing: border-box; margin: 0; padding: 0; }
  html, body { width: 849px; height: 1200px; overflow: hidden; background: var(--paper); }
  body { font-family: "Montserrat", Arial, sans-serif; color: var(--ink); }
  .page { position: relative; width: 849px; height: 1200px; }

  .brand-mark { position: absolute; left: 366px; top: 38px; }
  .brand-name {
    position: absolute; left: 0; width: 849px; top: 168px;
    text-align: center; font-size: 29px; font-weight: 400;
    letter-spacing: 1px; text-transform: uppercase; color: var(--ink);
  }
  .rule { position: absolute; top: 193px; height: 6px; background: var(--band); }
  .rule--left { left: 0; width: 268px; }
  .rule--right { left: 582px; width: 267px; }

  .title-band {
    position: absolute; left: 40px; top: 255px; width: 768px; height: 68px;
    background: var(--band); color: var(--paper);
    font-size: 25px; font-weight: 400; letter-spacing: .5px;
    display: flex; align-items: center; justify-content: center;
  }
  .title-band::after {
    content: ""; position: absolute; left: 0; right: 0; top: 68px; height: 8px;
    background: var(--grey-light);
  }

  .question { position: absolute; left: 40px; width: 768px; height: 61px; }
  .question__text {
    position: absolute; left: 0; top: 0; width: 364px; height: 61px;
    background: var(--grey); color: var(--paper);
    font-size: 15.5px; line-height: 17px; padding: 6px 20px 0 29px;
  }
  .question__tag {
    position: absolute; left: 373px; top: 1px; width: 94px; height: 26px;
    background: var(--grey); color: var(--paper);
    font-size: 15.5px; padding: 3px 0 0 11px;
  }
  .question__line {
    position: absolute; left: 476px; top: 0; width: 292px; height: 2px;
    background: var(--grey);
  }

  .phase { position: absolute; top: 770px; width: 249px; }
  .phase__head {
    height: 50px; background: var(--grey); color: var(--paper);
    text-align: center; font-size: 18.5px; line-height: 20px; padding-top: 4px;
  }
  .phase__box {
    position: absolute; left: 0; width: 249px; border: 1px solid var(--frame);
    padding: 9px 0 0 23px; font-size: 15.5px; line-height: 17.3px;
  }
  .phase__box--situation { top: 54px; height: 191px; }
  .phase__box--team { top: 249px; height: 142px; }
  .phase__box ul { list-style: none; }
  .phase__box li { padding-left: 13px; text-indent: -13px; }
  .phase__box li::before { content: "•"; display: inline-block; width: 13px; text-indent: 0; }
  .phase__box li span { padding-left: 9px; }
</style>
</head>
<body>
<div class="page">
  <svg class="brand-mark" width="117" height="117" viewBox="0 0 117 117" aria-hidden="true">
    <circle cx="58.5" cy="58.5" r="54" fill="none" stroke="#4a4a4c" stroke-width="7"/>
  </svg>
  <div class="brand-name">KR Allied Group</div>
  <div class="rule rule--left"></div>
  <div class="rule rule--right"></div>

  <div class="title-band">QUESTIONNAIRE</div>

  <div class="question" style="top:349px">
    <div class="question__text">Do you keep track of where all your money is spent?</div>
    <div class="question__tag">NOTES</div><div class="question__line"></div>
  </div>
  <div class="question" style="top:415px">
    <div class="question__text">Do you do your own tax return?</div>
    <div class="question__tag">NOTES</div><div class="question__line"></div>
  </div>
  <div class="question" style="top:481px">
    <div class="question__text">Do you have a preferred investment type (Shares, property, other)?</div>
    <div class="question__tag">NOTES</div><div class="question__line"></div>
  </div>
  <div class="question" style="top:546px">
    <div class="question__text">Do you have multiple super funds?</div>
    <div class="question__tag">NOTES</div><div class="question__line"></div>
  </div>
  <div class="question" style="top:612px">
    <div class="question__text">Do you have a home loan?</div>
    <div class="question__tag">NOTES</div><div class="question__line"></div>
  </div>
  <div class="question" style="top:678px">
    <div class="question__text">Do you have enough savings to fund your lifestyle if you couldn't work?</div>
    <div class="question__tag">NOTES</div><div class="question__line"></div>
  </div>

  <section class="phase" style="left:40px">
    <div class="phase__head">Phase 1<br>Starting out</div>
    <div class="phase__box phase__box--situation">
      Your situation:
      <ul>
        <li>Work full time</li>
        <li>Eliminate debt</li>
        <li>Save for first property</li>
        <li>Consider other investments and savings plans</li>
      </ul>
    </div>
    <div class="phase__box phase__box--team">
      Professionals involved:
      <ul>
        <li>Budget coach</li>
        <li>Financial adviser</li>
        <li>Accountant</li>
      </ul>
    </div>
  </section>

  <section class="phase" style="left:300px">
    <div class="phase__head">Phase 2<br>Laying the foundation</div>
    <div class="phase__box phase__box--situation">
      Your situation:
      <ul>
        <li>Purchased first home</li>
        <li>Start a family</li>
        <li>Protect assets</li>
        <li>Build investment portfolio</li>
        <li>Start planning for the future</li>
        <li>Implement correct tax structures</li>
      </ul>
    </div>
    <div class="phase__box phase__box--team">
      Professionals involved:
      <ul>
        <li>Budget coach</li>
        <li>Financial adviser</li>
        <li>Mortgage broker</li>
        <li>Accountant</li>
        <li>Conveyancer</li>
      </ul>
    </div>
  </section>

  <section class="phase" style="left:559px">
    <div class="phase__head">Phase 3<br>Break free</div>
    <div class="phase__box phase__box--situation">
      Your situation:
      <ul>
        <li>Pay off your residential home</li>
        <li>Purchase investment properties</li>
        <li>Grow investment portfolio</li>
        <li>Plan for retirement</li>
      </ul>
    </div>
    <div class="phase__box phase__box--team">
      Professionals involved:
      <ul>
        <li>Budget coach</li>
        <li>Financial adviser</li>
        <li>Mortgage broker</li>
        <li>Accountant</li>
        <li>Conveyancer</li>
        <li>Lawyer</li>
      </ul>
    </div>
  </section>
</div>
</body>
</html>
```